Website for Torvel Capital - investment banking firm

We have a corporate identity (thanks to Ranjita/41238) and want to extend that into a website design.  See the attached zipped files.
We have software folks in-house to do the coding.
See the attached Project Brief & Notes for more details.  Don't worry about the actual text - lorem ipsum will be fine.
The server will be Apache.
Thank you!
Desmond

```html
<!DOCTYPE html>
<html lang="en">
<head>
<meta charset="utf-8">
<title>Torvel Capital — Investment Banking</title>
<link rel="stylesheet" href="https://fonts.googleapis.com/css2?family=Cinzel:wght@400;700&family=Figtree:wght@400;600;700&family=Libre+Baskerville&display=swap">
<style>
:root{
  --brand:#0b5cb3;
  --brand-dark:#003f80;
  --nav-link:#8fc0f0;
  --white:#ffffff;
  --ink:#4a5666;
  --muted:#8a94a3;
  --footer-bg:#e3e7ef;
  --footer-head:#4d5a6b;
  --field:#9aaac2;
  --btn-dark:#2c4d7a;
}
*{box-sizing:border-box;margin:0;padding:0}
html,body{width:1145px;height:1200px;overflow:hidden;background:var(--white);font-family:"Figtree",sans-serif}
.page{position:relative;width:1145px;height:1200px}

.site-header{position:absolute;top:0;left:0;width:100%;height:78px;background:#fdfdfe}
.brand{position:absolute;left:153px;top:22px;display:flex;align-items:center;gap:12px}
.brand-mark{width:34px;height:34px;background:var(--brand)}
.brand-name{font-family:"Cinzel",serif;font-size:28px;font-weight:400;color:var(--brand);letter-spacing:.5px}

.main-nav{position:absolute;top:78px;left:0;width:100%;height:52px;background:var(--brand)}
.main-nav ul{list-style:none;display:flex;gap:33px;position:absolute;left:172px;top:18px}
.main-nav a{font-size:14.5px;font-weight:700;color:var(--nav-link);text-decoration:none;letter-spacing:.2px}
.main-nav a.active{color:var(--white)}

.hero{position:absolute;top:130px;left:0;width:100%;height:457px}
.hero-photo{position:absolute;inset:0;background:linear-gradient(100deg,#3b4440 0%,#6f7a78 40%,#8e959d 60%,#b9bfc6 80%,#7d858e 100%)}
.hero-caption{position:absolute;left:143px;top:128px;width:438px;height:222px;background:rgba(40,40,40,.55);padding:40px 0 0 46px}
.hero-caption h1{font-family:"Cinzel",serif;font-weight:400;font-size:29px;line-height:38px;color:var(--white);white-space:nowrap}
.hero-caption p{margin-top:22px;font-size:14.5px;line-height:21px;color:#e4e6ea;width:360px}
.slider-arrow{position:absolute;top:163px;width:49px;height:53px;background:rgba(40,40,40,.45);display:flex;align-items:center;justify-content:center}
.slider-arrow.prev{left:0}.slider-arrow.next{right:0}

.features{position:absolute;top:587px;left:143px;width:859px;height:267px;display:flex}
.feature{width:286.3px;height:100%;position:relative;padding:34px 0 0 30px;color:var(--white)}
.feature.who{background:linear-gradient(#0b5db3,#024283)}
.feature.services{background:linear-gradient(#0068cb,#0a4b95);padding-left:26px}
.feature.clients{background:linear-gradient(#4593e0,#2e68a5);padding-left:27px}
.feature h2{font-family:"Libre Baskerville",serif;font-weight:400;font-size:20px;margin-bottom:24px}
.feature p{font-size:11.3px;line-height:16.2px;width:232px}
.feature h3{font-size:11.3px;font-weight:700;margin-bottom:6px}
.feature ul{list-style:none}
.feature li{font-size:11.3px;line-height:22.4px;padding-left:9px;position:relative}
.feature li::before{content:"";position:absolute;left:0;top:7px;border-left:4px solid var(--white);border-top:4px solid transparent;border-bottom:4px solid transparent}
.read-more{position:absolute;left:37px;bottom:28px;width:71px;height:30px;border-radius:15px;background:var(--white);border:1px solid #c9d2de;font-size:10px;color:var(--muted);display:flex;align-items:center;justify-content:center}

.site-footer{position:absolute;top:940px;left:0;width:100%;height:218px;background:var(--footer-bg)}
.footer-col{position:absolute;top:33px}
.footer-col h4{font-size:11.5px;font-weight:700;letter-spacing:.6px;color:var(--footer-head);margin-top:14px;margin-bottom:14px}
.about{left:143px;top:34px}
.about .brand-name{font-size:20px}
.about .brand-mark{width:26px;height:26px}
.about p{font-size:11.3px;line-height:18px;color:var(--ink);margin:14px 0 0 5px;width:190px}
.about p+p{margin-top:18px}
.posts{left:372px}
.post{display:flex;gap:13px;margin-bottom:18px}
.post-thumb{width:49px;height:48px;background:linear-gradient(135deg,#6b7a8a,#c7cfd9)}
.post-text{font-size:11.3px;line-height:18px;color:var(--ink);width:135px}
.post-text time{display:block;font-size:9.5px;font-style:italic;color:var(--muted);line-height:16px}
.newsletter{left:600px}
.newsletter p{font-size:11.3px;line-height:20px;color:var(--ink);width:200px}
.subscribe{display:flex;margin-top:18px}
.subscribe .field{width:146px;height:33px;background:var(--field);color:var(--white);font-size:11.3px;padding:10px 0 0 12px}
.subscribe .btn{width:78px;height:33px;background:var(--btn-dark);color:var(--white);font-size:12.5px;display:flex;align-items:center;justify-content:center}
.contact{left:843px}
.contact li{list-style:none;display:flex;gap:13px;font-size:11.3px;line-height:17px;color:var(--ink);margin-bottom:10px}
.contact svg{flex:none;width:16px;height:16px}

.bottom-bar{position:absolute;top:1158px;left:0;width:100%;height:42px;background:var(--brand);color:var(--white);font-size:11.3px}
.bottom-bar .copy{position:absolute;left:148px;top:14px}
.bottom-bar .links{position:absolute;left:871px;top:14px;display:flex;gap:39px}
</style>
</head>
<body>
<div class="page">
  <header class="site-header">
    <div class="brand"><span class="brand-mark"></span><span class="brand-name">Torvel Capital</span></div>
  </header>

  <nav class="main-nav">
    <ul>
      <li><a class="active" href="#">HOME</a></li>
      <li><a href="#">HISTORY</a></li>
      <li><a href="#">CLIENTS</a></li>
      <li><a href="#">OUR TEAM</a></li>
      <li><a href="#">COMPLETED DEALS</a></li>
      <li><a href="#">CURRENT SEARCHES</a></li>
      <li><a href="#">CONTACT US</a></li>
    </ul>
  </nav>

  <section class="hero">
    <div class="hero-photo" role="img" aria-label="Photo of business people in suits talking at an outdoor gathering"></div>
    <div class="hero-caption">
      <h1>Global, Professional,<br>Trusted.</h1>
      <p>Torvel Capital is an independent investment bank working for buyers in a number of industries.</p>
    </div>
    <div class="slider-arrow prev"><svg width="12" height="18" viewBox="0 0 12 18"><path d="M10 2 3 9l7 7" fill="none" stroke="#fff" stroke-width="2.5"/></svg></div>
    <div class="slider-arrow next"><svg width="12" height="18" viewBox="0 0 12 18"><path d="M2 2l7 7-7 7" fill="none" stroke="#fff" stroke-width="2.5"/></svg></div>
  </section>

  <section class="features">
    <article class="feature who">
      <h2>Who We Are</h2>
      <p>Torvel Capital is an independent investment bank working for buyers in a number of industries. We utilize exceptional technology in finding companies to meet our client's search criteria. We will not waste a buyer's time, a seller's time, or our own time.</p>
      <span class="read-more">Read More</span>
    </article>
    <article class="feature services">
      <h2>Our Services</h2>
      <h3>OUR SERVICES INCLUDE::</h3>
      <ul>
        <li>Buy-Side Acquisitions</li>
        <li>Recapitalizations &amp; Growth Capital Partnerships</li>
        <li>Sell-Side Transactions</li>
      </ul>
      <span class="read-more">Read More</span>
    </article>
    <article class="feature clients">
      <h2>Our Clients</h2>
      <p>Torvel Capital has a diverse array of clients ranging from multi-billion dollar strategic acquirers to large private equity funds. We will not engage a client as a buyer if we believe there is any chance of them wasting our time or a prospective seller's time.</p>
      <span class="read-more">Read More</span>
    </article>
  </section>

  <footer class="site-footer">
    <div class="footer-col about">
      <div class="brand" style="position:static"><span class="brand-mark"></span><span class="brand-name">Torvel Capital</span></div>
      <p>Donec volutpat, mi vel egestas eleif-end, dolor arcu iaculis nunc. Fusce gravida tortor felis, ac dictum risus</p>
      <p>sagittis id. Morbi posuere justo eleif-end libero ultricies ultrices.</p>
    </div>
    <div class="footer-col posts">
      <h4>RECENT POST</h4>
      <div class="post"><div class="post-thumb" role="img" aria-label="Thumbnail photo of two business people"></div><div class="post-text">Fusce gravida tortor felis, ac dictum risus sagittis<time>October 15, 2013</time></div></div>
      <div class="post"><div class="post-thumb" role="img" aria-label="Thumbnail photo of hands holding a tablet"></div><div class="post-text">Fusce gravida tortor felis, ac dictum risus sagittis<time>October 15, 2013</time></div></div>
    </div>
    <div class="footer-col newsletter">
      <h4>NEWSLETTER</h4>
      <p>Ipsum dolor sit amet, teft consecte tur adipiscing elit ut eunt.</p>
      <div class="subscribe"><span class="field">Email Address</span><span class="btn">Subscribe</span></div>
    </div>
    <div class="footer-col contact">
      <h4>CONTACT DETAILS</h4>
      <ul>
        <li><svg viewBox="0 0 16 16"><path d="M4 1.5 6 5 4.6 6.6c.8 1.9 2.4 3.5 4.4 4.6L10.6 10l3.4 2-1.3 2.5C7.5 14.4 1.6 8.5 1.5 3.3Z" fill="#7b8594"/></svg>+1800-555-0147</li>
        <li><svg viewBox="0 0 16 16"><rect x="1.5" y="3.5" width="13" height="9.5" fill="none" stroke="#7b8594" stroke-width="1.4"/><path d="m2 4 6 5 6-5" fill="none" stroke="#7b8594" stroke-width="1.4"/></svg>info@torvelcapital.com</li>
        <li><svg viewBox="0 0 16 16"><path d="M8 1a4.5 4.5 0 0 0-4.5 4.5C3.5 9 8 15 8 15s4.5-6 4.5-9.5A4.5 4.5 0 0 0 8 1Zm0 6.2a1.7 1.7 0 1 1 0-3.4 1.7 1.7 0 0 1 0 3.4Z" fill="#7b8594"/></svg>Your Address, Your Country<br>Your Zip Code</li>
      </ul>
    </div>
  </footer>

  <div class="bottom-bar">
    <span class="copy">Copyright © 2014 - TorvelCapital. All Rights reserved</span>
    <span class="links"><span>Privacy Policy</span><span>Sitemap</span></span>
  </div>
</div>
</body>
</html>
```